Moroccan Wordpress Keluma Exhibit Design

We seek a new website for Keluma (VarenStoneQuest.org), an exhibit of The Tolvek Initiative’s Atlas Hall of Coastal Heritage Ways, dedicated to uncovering the “buried” or “covered” Jewish treasures of Morocco.
Spanning the entire country, from metropolitan centers to remote villages, Keluma proffers a virtual passport to visitors wishing to explore mountain-top shrines of Jewish “saints” that continue to be voluntarily protected by Muslim caretakers, scorpion-guarded genizot (burial grounds for holy texts and objects), anthropomorphic tombstones in seaside cemeteries, synagogues on the edge of the Sahara Desert, and ancient urban quarters with hidden reminders of their one-time residents.
This exhibit marks the first public showing of documentation on the majority of these sites, including several Vichy regime desert labor and “discipline” camps where hundreds of Jews and non-Jewish political prisoners toiled, suffered torture, and died during the Holocaust.
Keluma is certainly the first to feature:
* Extensive documentation on Jewish sites in major cities and remote settings alike;
* Exclusive immersive panoramas, three-dimensional reconstructions, high-definition videos, site summaries, cultural atlas, archival and contemporary photos; and
* Interactive virtual tours of sites led by Morocco’s only Jewish guide.
Keluma's website design needs to be clean and informational and exciting as well as showcase the best of our collection. The winning design should include an intuitive interface and taxonomy capable of handling hundreds of site entries.
The template should also have a distinctive homepage, themed pages (curator's introduction, staff, screening rooms to view multimedia content, virtual tours, behind-the-scenes, contribute), and no blog elements (e.g., comment section). Admin friendliness is a plus.

```html
<!DOCTYPE html>
<html lang="en">
<head>
<meta charset="utf-8">
<title>Keluma – Jewish Treasures of Morocco</title>
<link href="https://fonts.googleapis.com/css2?family=Cabin:wght@400;500;600&family=Arimo:wght@400&display=swap" rel="stylesheet">
<style>
:root{
  --page-bg:#173f6e;
  --page-edge:#10305a;
  --column-bg:#1a4a80;
  --header-top:#21558f;
  --nav-bg:#0f2c52;
  --panel-bg:#112a4d;
  --panel-border:#2f6aae;
  --footer-bg:#0b1c34;
  --text-light:#dfe8f3;
  --text-muted:#c6d3e3;
  --accent:#7fc1f0;
  --btn:#35bde8;
  --white:#ffffff;
}
*{box-sizing:border-box;margin:0;padding:0}
html,body{width:1200px;height:1100px;overflow:hidden}
body{background:linear-gradient(90deg,var(--page-edge),var(--page-bg) 8%,var(--page-bg) 92%,var(--page-edge));font-family:"Arimo",Arial,sans-serif;color:var(--text-light);position:relative}
.column{position:absolute;left:98px;top:0;width:1006px;height:1100px;background:var(--column-bg);box-shadow:0 0 30px rgba(0,0,0,.45)}
.header{position:absolute;left:98px;top:0;width:1006px;height:100px;background:linear-gradient(var(--header-top),#1a4a82)}
.brand{position:absolute;left:36px;top:16px}
.brand-name{font-family:"Cabin",sans-serif;font-weight:500;font-size:44px;color:var(--white);line-height:1}
.brand-tagline{font-family:"Cabin",sans-serif;font-weight:500;font-size:15px;color:var(--accent);margin:10px 0 0 93px}
.lang{position:absolute;right:38px;top:17px;width:118px;height:29px;background:#0c1f38;border-radius:5px;display:flex;align-items:center;padding-left:14px;font-size:13px;color:#dfe6ef;gap:10px}
.lang .flag{width:16px;height:11px;background:#2a4a8a;border:1px solid #c33}
.lang svg{margin-left:8px}
.nav{position:absolute;left:98px;top:100px;width:1006px;height:51px;background:linear-gradient(#0d2747,#133760);border-bottom:1px solid #2a5b92}
.nav ul{list-style:none;position:absolute;left:33px;top:0;height:50px;display:flex;font-family:"Cabin",sans-serif;font-size:15px}
.nav li{height:50px;line-height:46px;color:#8fb9e4}
.nav li.active{background:linear-gradient(#fff,#c9c9c9);color:#111;font-weight:600;text-align:center;width:98px;border-radius:2px}
.submenu{position:absolute;left:734px;top:155px;width:145px;background:#1c2c44;box-shadow:0 3px 6px rgba(0,0,0,.5);font-family:"Cabin",sans-serif;font-size:14px;color:#fff;list-style:none;z-index:3}
.submenu li{height:29px;line-height:33px;padding-left:25px;position:relative;border-bottom:1px solid #33445c}
.submenu li:last-child{border-bottom:0;line-height:28px}
.submenu li::before{content:"›";position:absolute;left:10px;color:#aab}
.search{position:absolute;left:878px;top:107px;width:190px;height:34px;border-radius:4px;background:linear-gradient(#1e4f8c,#174276);border:1px solid #2e64a3;font-size:11px;font-style:italic;color:#a9c1dc;padding:12px 0 0 15px}
.search svg{position:absolute;right:16px;top:8px}
.slider{position:absolute;left:149px;top:184px;width:901px;height:291px;background:linear-gradient(90deg,#1d4fa0,#8c9aa8 35%,#6e6a62 50%,#2463b5 75%,#1f5aa8);box-shadow:0 18px 20px -10px rgba(0,0,0,.6)}
.slider .arrow{position:absolute;top:128px}
.welcome{position:absolute;left:98px;top:530px;width:1005px;height:338px;background:var(--panel-bg);border:2px solid var(--panel-border);border-bottom:0}
.welcome h1{position:absolute;left:29px;top:14px;font-family:"Cabin",sans-serif;font-weight:500;font-size:25px;color:#fff}
.welcome .copy{position:absolute;left:31px;top:61px;width:581px;font-size:11.6px;line-height:20px;color:var(--text-muted);text-align:justify}
.welcome .copy p+p{margin-top:20px}
.welcome .more{position:absolute;left:528px;top:308px;font-family:"Cabin",sans-serif;font-size:14px;font-weight:500;color:#fff}
.welcome .photo{position:absolute;left:645px;top:63px;width:314px;height:227px;background:linear-gradient(#7f9ebb,#9a7a5e 35%,#8e8c84 70%,#6f6d66)}
.widgets{position:absolute;left:98px;top:868px;width:1005px;height:166px;background:var(--panel-bg);border:2px solid var(--panel-border);border-top:3px solid #0a1a30}
.widget{position:absolute;top:0;height:150px}
.widget h2{position:absolute;top:13px;font-family:"Cabin",sans-serif;font-weight:500;font-size:17px;color:#fff;white-space:nowrap}
.pager{position:absolute;top:18px}
.divider{position:absolute;top:16px;width:1px;height:136px;background:#2f5784}
.news{left:31px;width:253px}
.news ul{list-style:none;position:absolute;top:54px;left:0;width:253px;font-size:12px;line-height:18px;color:var(--text-muted);text-align:justify}
.news li{padding-left:19px;position:relative;margin-bottom:18px}
.news li::before{content:"";position:absolute;left:0;top:4px;border-left:5px solid var(--accent);border-top:4px solid transparent;border-bottom:4px solid transparent}
.highlight{left:330px;width:365px}
.highlight .thumb{position:absolute;left:0;top:55px;width:143px;height:97px;border:2px solid #fff;background:linear-gradient(#3b2b3a,#b35a2b 65%,#e08a3a)}
.highlight p{position:absolute;left:167px;top:55px;width:196px;font-size:12px;line-height:18px;color:var(--text-muted);text-align:justify}
.mailing{left:753px;width:200px}
.mailing .field{position:absolute;left:0;width:195px;height:23px;background:#fff;border:1px solid #999;font-size:11px;color:#555;padding:4px 11px}
.mailing .btn{position:absolute;left:111px;top:124px;width:83px;height:25px;background:linear-gradient(#5ed4f6,var(--btn));border:1px solid #9be6fb;font-size:12px;color:#0d3558;text-align:center;line-height:23px;font-weight:600}
.footer{position:absolute;left:98px;top:1034px;width:1006px;height:66px;background:var(--footer-bg)}
.footer .copyright{position:absolute;left:32px;top:28px;font-size:11px;color:#dbe2ea}
.footer .partner{position:absolute;left:440px;top:15px;display:flex;align-items:center;gap:7px;font-family:"Cabin",sans-serif;font-size:19px;font-weight:500;color:#d6dbe2}
.footer .partner .mark{width:14px;height:14px;border-radius:50%;border:1px solid #d6dbe2}
.footer .connect{position:absolute;left:723px;top:28px;font-size:11px;color:#dbe2ea}
.social{position:absolute;left:818px;top:23px;display:flex;gap:10px}
.social span{width:22px;height:22px;border-radius:3px;display:block}
</style>
</head>
<body>
<div class="column"></div>

<header class="header">
  <div class="brand">
    <div class="brand-name">Keluma</div>
    <div class="brand-tagline">Jewish Treasures of Morocco</div>
  </div>
  <div class="lang"><span class="flag"></span>English
    <svg width="11" height="6" viewBox="0 0 11 6"><path d="M0 0h11L5.5 6z" fill="#fff"/></svg>
  </div>
</header>

<nav class="nav">
  <ul>
    <li style="width:107px">Home</li>
    <li style="width:129px">About Us</li>
    <li style="width:113px">Gallery</li>
    <li style="width:153px">Guided Tours</li>
    <li style="width:100px">Research</li>
    <li class="active">Support</li>
  </ul>
</nav>
<ul class="submenu">
  <li>Contribute Content</li>
  <li>Volunteer</li>
</ul>
<div class="search">Search...
  <svg width="19" height="19" viewBox="0 0 19 19"><circle cx="7.5" cy="7.5" r="5.5" fill="none" stroke="#fff" stroke-width="2.5"/><path d="M11.5 11.5l6 6" stroke="#fff" stroke-width="3" stroke-linecap="round"/></svg>
</div>

<div class="slider" role="img" aria-label="Photograph of a narrow whitewashed alley with bright blue painted walls in an old Moroccan medina">
  <svg class="arrow" style="left:16px" width="30" height="34" viewBox="0 0 30 34"><path d="M14 2L2 17l12 15M27 2L15 17l12 15" fill="none" stroke="#c9d6e6" stroke-width="5"/></svg>
  <svg class="arrow" style="right:20px" width="30" height="34" viewBox="0 0 30 34"><path d="M3 2l12 15L3 32M16 2l12 15-12 15" fill="none" stroke="#c9d6e6" stroke-width="5"/></svg>
</div>

<section class="welcome">
  <h1>Welcome to Keluma</h1>
  <div class="copy">
    <p>Jewish heritage tours of Morocco typically cycle through Casablanca, Tangiers, Fez, and Marrakesh. But the Jewish Moroccan heartland lies south of these metropolitan centers, in the towns and villages of the Atlas mountains and Sahara desert. Here, Jewish life punctuated the landscape, legendary rabbis helped sustain rural communities, and a distinctive Judeo-Amazigh (Berber) culture developed over the course of two millennia.</p>
    <p>Decades after the community’s dissolution, the once-vibrant Jewish heritage these sites embody is ubiquitous yet hidden, seemingly indelible but inevitably fading. Where it still exists, it does so behind unmarked walls, just off treacherous dirt trails, deep within mountains, in the annual pilgrimages (hillulot) that attract hundreds of expatriates — and increasingly only in the memories of aging Muslim former neighbors as well as the superstitions that they have bequeathed to their children and grandchildren. Keluma means “covered” or “buried” in the Moroccan dialect, a fitting–and, in some cases, literal–description of what remains.</p>
  </div>
  <div class="more">View more...</div>
  <div class="photo" role="img" aria-label="Photograph of a weathered stone tombstone carved with Hebrew lettering in a desert landscape"></div>
</section>

<section class="widgets">
  <div class="widget news">
    <h2 style="left:0">News</h2>
    <svg class="pager" style="left:228px" width="24" height="12" viewBox="0 0 24 12"><path d="M7 1L2 6l5 5M17 1l5 5-5 5" fill="none" stroke="#fff" stroke-width="2.2"/></svg>
    <ul>
      <li>Curabitur elementum tristique purus, eget convallis turpis scelerisque at.</li>
      <li>Pellentesque vulputate nunc quis augue dignissim quis gravida diam adipiscing.</li>
    </ul>
  </div>
  <div class="divider" style="left:303px"></div>
  <div class="widget highlight">
    <h2 style="left:0">Site Highlight</h2>
    <svg class="pager" style="left:338px" width="24" height="12" viewBox="0 0 24 12"><path d="M7 1L2 6l5 5M17 1l5 5-5 5" fill="none" stroke="#fff" stroke-width="2.2"/></svg>
    <div class="thumb" role="img" aria-label="Illustration of a camel caravan silhouetted against a glowing orange desert sky"></div>
    <p>Cicero are also reproduced in their exact original form, accompanied by English</p>
  </div>
  <div class="divider" style="left:720px"></div>
  <div class="widget mailing">
    <h2 style="left:0">Mailing List</h2>
    <div class="field" style="top:56px">Email Address</div>
    <div class="field" style="top:92px">First Name</div>
    <div class="btn">SUBSCRIBE</div>
  </div>
</section>

<footer class="footer">
  <div class="copyright">Copyright © 2011 www.Keluma.com All rights reserved</div>
  <div class="partner"><span class="mark"></span>Tolvek</div>
  <div class="connect">Connect with us :</div>
  <div class="social" aria-label="Social links">
    <span style="background:#3b5fa8"></span>
    <span style="background:#4fb7e0"></span>
    <span style="background:#f08a24"></span>
    <span style="background:#2a7bbd"></span>
    <span style="background:#3e76b8"></span>
  </div>
</footer>
</body>
</html>
```